public page walrus GX (www.walrusgx.com)

https://www.quillbarn.net/shard/s412/sh/a3b1c9d2-58e4-4f7a-b2c6-1d9e0f7a3b45/41c7e2a9d08b6f53e17a92c4d6b0f831

compatible with wordpress

Designs look the same

Industry/Entity Type

Finance And Accounting

Coding

Coded - Design and coding required

Number of Pages Required

1 page

Font styles to use
Sans Serif

Colors
85cae6
3176b5
cfdeed
fac994
fff3d1
fefdec
cfcfcf
e8e8e8
9d9d9d

```html
<!DOCTYPE html>
<html lang="en">
<head>
<meta charset="utf-8">
<title>walrus GX — Profit calculator for Bazaaro sellers</title>
<link href="https://fonts.googleapis.com/css2?family=Ubuntu:wght@400;500;700&family=Lato:wght@400;700;900&display=swap" rel="stylesheet">
<style>
:root{
  --hero-bg:#e4ecfb;
  --features-bg:#fdeae4;
  --footer-bg:#fde2d5;
  --purple:#5a4898;
  --ink:#4a4a5a;
  --muted:#6b6b78;
  --blue:#3176b5;
  --sky:#85cae6;
  --coral:#f4857a;
  --peach:#fac994;
  --white:#ffffff;
  --line:#e9cfc4;
}
*{margin:0;padding:0;box-sizing:border-box}
html,body{width:1200px;height:4255px;overflow:hidden}
body{position:relative;font-family:"Lato",sans-serif;color:var(--ink);background:var(--features-bg)}
.abs{position:absolute}
.hero{position:absolute;left:0;top:0;width:1200px;height:1340px;background:var(--hero-bg)}
.features{position:absolute;left:0;top:1340px;width:1200px;height:2530px;background:linear-gradient(180deg,#fdf0ec,var(--features-bg))}
.site-footer{position:absolute;left:0;top:3870px;width:1200px;height:385px;background:var(--footer-bg)}

.brand{left:38px;top:28px;display:flex;align-items:center;gap:10px}
.brand-mark{width:34px;height:34px;border-radius:50%;background:var(--purple)}
.brand-name{font-family:"Ubuntu",sans-serif;font-weight:500;font-size:22px;color:var(--purple)}
.main-nav{left:425px;top:48px;display:flex;align-items:center;gap:28px;font-size:13px;font-weight:700;letter-spacing:.5px;color:var(--ink)}
.main-nav .current{color:var(--blue)}
.nav-btn{padding:7px 16px;border-radius:16px;font-size:12px}
.nav-btn.outline{border:1.5px solid var(--blue);color:var(--blue)}
.nav-btn.fill{background:var(--peach);color:var(--ink)}
.menu-toggle{width:36px;height:36px;border-radius:6px;background:var(--purple);display:flex;flex-direction:column;justify-content:center;align-items:center;gap:4px}
.menu-toggle span{width:16px;height:2px;background:var(--white)}

.art{border-radius:24px}
.hero-art{left:30px;top:190px;width:480px;height:500px;background:radial-gradient(ellipse at 50% 85%,#8fb1c9 0,#b9cde6 40%,var(--hero-bg) 72%)}
.hero-title{left:745px;top:248px;width:420px;font-family:"Ubuntu",sans-serif;font-size:35px;line-height:1.25;color:var(--purple)}
.email-field{left:740px;top:424px;width:400px;height:46px;border-radius:23px;background:var(--white);display:flex;align-items:center;justify-content:center;font-size:14px;color:var(--muted)}
.btn{display:flex;align-items:center;justify-content:center;color:var(--white);font-size:15px;font-weight:700;border-radius:23px}
.hero-cta{left:840px;top:484px;width:202px;height:46px;background:var(--blue)}
.watch{left:852px;top:600px;display:flex;align-items:center;gap:10px;font-weight:900;font-size:15px;letter-spacing:.5px;color:var(--ink)}

.tagline{left:0;top:812px;width:1200px;text-align:center;font-family:"Ubuntu",sans-serif;font-size:38px;line-height:1.3;color:var(--purple)}
.intro{left:130px;top:955px;width:940px;text-align:center;font-size:18px;line-height:1.45;color:var(--ink)}
.partners{left:92px;top:1097px;display:flex;gap:35px}
.partner{width:228px;height:130px;background:var(--white);border-radius:4px;box-shadow:0 4px 14px rgba(90,72,152,.12);display:flex;align-items:center;justify-content:center}
.partner i{display:block;width:120px;height:34px;border-radius:6px;background:#dfe5ef}

.feature-title{font-family:"Ubuntu",sans-serif;font-size:40px;color:var(--purple)}
.feature-text{font-size:18px;line-height:1.4;color:var(--muted);width:540px}
.art-keywords{left:690px;top:1460px;width:390px;height:290px;background:radial-gradient(circle,#9ec7de 0,#f3c9b3 55%,var(--features-bg) 75%)}
.art-sales{left:140px;top:1860px;width:350px;height:250px;background:linear-gradient(90deg,#7fb3d0,#c98a4f 60%,#a0643a)}
.art-ppc{left:690px;top:2275px;width:370px;height:250px;background:linear-gradient(135deg,#3d6d8a,#7aa9c5 50%,#f3d0b8)}
.art-success{left:175px;top:2710px;width:430px;height:310px;background:linear-gradient(135deg,#3e4a5e,#e86a5d 55%,#f5c55a)}

.perks{left:0;top:3205px;width:1200px;display:flex;justify-content:center;gap:80px}
.perk{width:280px;text-align:center}
.perk svg{display:block;margin:0 auto 22px}
.perk h3{font-size:18px;font-weight:700;color:var(--purple);margin-bottom:10px}
.perk p{font-size:17px;line-height:1.3;color:var(--muted)}

.pricing{left:0;top:3545px;width:1200px;text-align:center;font-family:"Ubuntu",sans-serif;color:var(--purple)}
.pricing h2{font-weight:400;font-size:48px;line-height:1.15}
.pricing strong{font-size:52px;font-weight:700}
.pricing-cta{left:497px;top:3700px;width:203px;height:46px;background:var(--coral)}

.footer-brand{left:90px;top:3930px;display:flex;flex-direction:column;align-items:center;gap:14px}
.footer-brand .brand-mark{width:80px;height:80px}
.footer-brand .brand-name{font-size:26px;letter-spacing:1px;color:var(--blue)}
.socials{left:95px;top:4090px;display:flex;gap:14px}
.socials span{width:30px;height:30px;border-radius:50%;background:var(--white);border:1.5px solid #e6c6b8}
.col-title{font-size:19px;font-weight:700;color:var(--purple)}
.links{display:grid;grid-template-columns:150px 200px;row-gap:6px;font-size:17px;color:var(--muted)}
.contact-list{font-size:17px;color:var(--muted);display:flex;flex-direction:column;gap:26px}
.contact-list div{display:flex;align-items:center;gap:8px}
.footer-rule{left:90px;top:4190px;width:1020px;height:1px;background:var(--line)}
.copyright{left:0;top:4212px;width:1200px;text-align:center;font-size:11px;letter-spacing:.5px;color:var(--ink)}
</style>
</head>
<body>

<section class="hero">
  <div class="abs brand"><span class="brand-mark"></span><span class="brand-name">walrus GX</span></div>
  <nav class="abs main-nav">
    <span class="current">● HOME</span><span>PRICING</span><span>ABOUT</span><span>CONTACT</span><span>BLOG</span><span>FAQs</span>
    <span class="nav-btn outline">SIGN UP</span><span class="nav-btn fill">SIGN IN</span>
    <span class="menu-toggle"><span></span><span></span><span></span></span>
  </nav>

  <div class="abs art hero-art" role="img" aria-label="Illustration of a team of sellers holding coin signs around a piggy bank and a marketplace browser window"></div>
  <h1 class="abs hero-title">We are building a simple and intuitive service for Bazaaro sellers to calculate their profit.</h1>
  <div class="abs email-field">Enter Your Email Address</div>
  <div class="abs btn hero-cta">Get Started</div>
  <div class="abs watch">
    <svg width="26" height="26" viewBox="0 0 26 26"><circle cx="13" cy="13" r="11" fill="none" stroke="#4a4a5a" stroke-width="1.8"/><path d="M10.5 8.5v9l7-4.5z" fill="#4a4a5a"/></svg>
    WATCH VIDEO
  </div>

  <p class="abs tagline">Profit is not something to add on at the end,<br>it is something to plan for in the beginning</p>
  <p class="abs intro"><b>WALRUS GX</b> is the first ever software created by <b>Real Needs</b> of the <b>Real Bazaaro Sellers</b> in cooperation with group of brilliant software engineers to help you manage your business and calculate your <b>Real Profit</b> on everyday basis.</p>
  <div class="abs partners">
    <div class="partner"><i></i></div><div class="partner"><i></i></div><div class="partner"><i></i></div><div class="partner"><i></i></div>
  </div>
</section>

<section class="features">
</section>

<div class="abs art art-keywords" role="img" aria-label="Illustration of a magnifying glass surrounded by keyword and analytics icons"></div>
<h2 class="abs feature-title" style="left:142px;top:1520px">Find new keywords</h2>
<p class="abs feature-text" style="left:142px;top:1593px">Lorem ipsum dolor sit amet, consectetur adipiscing elit, sed do eiusmod tempor incididunt ut labore et do lore magna aliqua. Ut enim ad minim veniam, quis nos trud exercitation ullamco laboris nisi ut aliquip.</p>

<div class="abs art art-sales" role="img" aria-label="Illustration of a person running up rising bar columns"></div>
<h2 class="abs feature-title" style="left:590px;top:1935px">Boost your sales</h2>
<p class="abs feature-text" style="left:590px;top:2008px;width:490px">Lorem ipsum dolor sit amet, consectetur adipis cing elit, sed do eiusmod tempor incididunt ut la bore et dolore magna aliqua. Ut enim ad minim veniam, quis nos trud exercitation.</p>

<div class="abs art art-ppc" role="img" aria-label="Illustration of a hand pressing a laptop showing ad campaign screens"></div>
<h2 class="abs feature-title" style="left:142px;top:2352px">Automate PPC Campaign</h2>
<p class="abs feature-text" style="left:142px;top:2425px;width:490px">Lorem ipsum dolor sit amet, consectetur adipis cing elit, sed do eiusmod tempor incididunt ut la bore et dolore magna aliqua. Ut enim ad minim veniam, quis nos trud exercitation.</p>

<div class="abs art art-success" role="img" aria-label="Illustration of a rocket launching from a laptop with a hand holding a phone"></div>
<h2 class="abs feature-title" style="left:697px;top:2775px;line-height:1.2">Success and make<br>profit on Bazaaro</h2>
<p class="abs feature-text" style="left:697px;top:2900px;width:380px">Lorem ipsum dolor sit amet, consecte tur adipiscing elit, sed do eiusmod tempor incididu ut labore et dolore magna aliqua.</p>

<div class="abs perks">
  <div class="perk">
    <svg width="76" height="60" viewBox="0 0 76 60" fill="none" stroke="#f4857a" stroke-width="3"><rect x="6" y="36" width="10" height="20"/><rect x="24" y="28" width="10" height="28"/><rect x="42" y="20" width="10" height="36"/><rect x="60" y="12" width="10" height="44"/><path d="M4 28 22 16l14 6 26-18"/><path d="M56 4h8v8"/></svg>
    <h3>Complete Data Analytics</h3>
    <p>Lorem ipsum dolor sit amet, consectetur adipiscing elit, sed do eiusmod tempor inci didu ut labore et dolore.</p>
  </div>
  <div class="perk">
    <svg width="60" height="60" viewBox="0 0 60 60" fill="none" stroke="#f4857a" stroke-width="3"><rect x="6" y="6" width="48" height="48" rx="4"/><circle cx="30" cy="26" r="12"/><rect x="24" y="24" width="12" height="10" rx="1"/><path d="M26 24v-4a4 4 0 0 1 8 0v4"/><path d="M14 46h32"/></svg>
    <h3>Security and Privacy</h3>
    <p>Lorem ipsum dolor sit amet, consectetur adipiscing elit, sed do eiusmod tempor inci didu ut labore et dolore.</p>
  </div>
  <div class="perk">
    <svg width="60" height="60" viewBox="0 0 60 60" fill="none" stroke="#f4857a" stroke-width="3"><circle cx="30" cy="26" r="14"/><path d="M12 28v-4a18 18 0 0 1 36 0v4"/><rect x="8" y="24" width="6" height="12" rx="2"/><rect x="46" y="24" width="6" height="12" rx="2"/><path d="M14 56c2-8 8-12 16-12s14 4 16 12"/></svg>
    <h3>Expert Support</h3>
    <p>Lorem ipsum dolor sit amet, consectetur adipiscing elit, sed do eiusmod tempor inci didu ut labore et dolore.</p>
  </div>
</div>

<div class="abs pricing">
  <h2>Complete analytics solutions only</h2>
  <strong>$2.95/month*</strong>
</div>
<div class="abs btn pricing-cta">Get Started</div>

<footer class="site-footer"></footer>
<div class="abs footer-brand"><span class="brand-mark"></span><span class="brand-name">WALRUS GX</span></div>
<div class="abs socials"><span></span><span></span><span></span><span></span></div>

<h4 class="abs col-title" style="left:430px;top:3925px">Quick Links</h4>
<div class="abs links" style="left:430px;top:3975px">
  <span>Home</span><span>FAQs</span>
  <span>Pricing</span><span>Sign Up</span>
  <span>About Us</span><span>Sign In</span>
  <span>Contact</span><span>Privacy Policy</span>
  <span>Blog</span><span>Terms &amp; Conditions</span>
</div>

<h4 class="abs col-title" style="left:893px;top:3925px">Contact</h4>
<div class="abs contact-list" style="left:893px;top:3980px">
  <div><svg width="16" height="18" viewBox="0 0 16 18" fill="none" stroke="#6b6b78" stroke-width="1.6"><path d="M8 17s6-6 6-10A6 6 0 0 0 2 7c0 4 6 10 6 10z"/><circle cx="8" cy="7" r="2"/></svg>+1 555-014-0392</div>
  <div><svg width="16" height="16" viewBox="0 0 16 16" fill="none" stroke="#6b6b78" stroke-width="1.6"><circle cx="8" cy="8" r="7"/><path d="M5 4.5c0 4 2.5 6.5 6.5 6.5l-.5-2-2 .3-2.3-2.3.3-2z"/></svg>info@walrusgx.com</div>
</div>

<div class="abs footer-rule"></div>
<p class="abs copyright">COPYRIGHT © 2016 WALRUSGX. ALL RIGHTS RESERVED.</p>

</body>
</html>
```